business card design for a small scale specialty cut flower farm

We need a business card design for Hollowmere Bloom Farm based in Langley, BC, Canada. We produce specialty, high-end cut flowers and sell locally to florists, local shops and markets and the end user through bouquet subscriptions. The final business card design should be memorable and have a timeless or vintage feel. We would prefer a square shape.
Updates

Target Market(s)

florists, shops and seasonal markets, local flower lovers

Industry/Entity Type

Floral

Contact Information for Business Card

Tamsin Ellery Voss, Grower
Langley, BC, Canada
website: hollowmerebloomfarm.example
instagram: @hollowmerebloomfarm
Tel: 555.317.4290
facebook: www.facebook.example/hollowmereblooms/

Font styles to use
Serif
Decorative
Script

Requirements
Must have
• soft black background colour on front side, the included logo and catch phrase: Fresh Local Seasonal
Nice to have
• phone number and website address on front of card, included photo 6539 incorporated onto the back, possibly photo 6609 as well.

```html
<!DOCTYPE html>
<html lang="en">
<head>
<meta charset="utf-8">
<title>Hollowmere Bloom Farm — Business Card</title>
<link href="https://fonts.googleapis.com/css2?family=Cormorant+Garamond:ital,wght@0,400;0,500;1,400&family=Lato:wght@400&display=swap" rel="stylesheet">
<style>
  :root {
    --stage: #e3e4e6;
    --soft-black: #2a2928;
    --soft-black-glow: #343231;
    --paper: #dfe3e3;
    --ink: #1d1d1f;
    --ink-soft: #3a3a3d;
    --accent: #4a4644;
    --petal: #e9a9cc;
    --mist: #c9c3c4;
    --white: #ffffff;
  }
  * { box-sizing: border-box; margin: 0; padding: 0; }
  html, body {
    width: 1200px; height: 1200px; overflow: hidden;
    background: var(--stage);
  }
  .stage {
    width: 1200px; height: 1200px;
    display: flex; align-items: center; justify-content: center; gap: 60px;
  }
  .card {
    position: relative;
    width: 520px; height: 520px;
    box-shadow: 0 18px 30px rgba(0,0,0,0.18);
    overflow: hidden;
  }

  /* Front */
  .card-front {
    background: var(--soft-black);
    color: var(--white);
    text-align: center;
  }
  .front-pattern {
    position: absolute; inset: 0;
    background: radial-gradient(circle at 50% 45%, var(--soft-black-glow), var(--soft-black) 70%);
  }
  .front-lockup {
    position: absolute; left: 0; right: 0; top: 118px;
    display: flex; flex-direction: column; align-items: center;
  }
  .brand-dot {
    width: 92px; height: 92px; border-radius: 50%;
    background: var(--petal);
    margin-bottom: 26px;
  }
  .brand-name {
    font-family: 'Cormorant Garamond', serif;
    font-weight: 500;
    font-size: 44px;
    line-height: 1.05;
    color: var(--white);
  }
  .tagline {
    margin-top: 16px;
    font-family: 'Cormorant Garamond', serif;
    font-style: italic;
    font-size: 19px;
    color: var(--mist);
  }
  .established {
    margin-top: 12px;
    font-family: 'Lato', sans-serif;
    font-size: 11px;
    letter-spacing: 4px;
    color: var(--mist);
  }

  /* Back */
  .card-back {
    background: var(--paper);
    color: var(--ink);
  }
  .back-brand {
    position: absolute; right: 62px; top: 58px;
    font-family: 'Cormorant Garamond', serif;
    font-weight: 500;
    font-size: 26px;
    line-height: 1.1;
    text-align: right;
    color: var(--ink);
  }
  .contact-block {
    position: absolute; left: 78px; top: 238px;
    font-family: 'Cormorant Garamond', serif;
  }
  .person-name {
    font-size: 27px; font-weight: 500; letter-spacing: 0.5px;
    color: var(--ink);
  }
  .person-role {
    font-size: 25px; font-style: italic;
    color: var(--accent);
    margin-top: 2px;
  }
  .contact-list {
    list-style: none;
    margin-top: 30px;
    font-size: 18.5px;
    line-height: 1.25;
    color: var(--ink-soft);
    letter-spacing: 0.3px;
  }
  .contact-list .gap { margin-top: 22px; }
</style>
</head>
<body>
<main class="stage">
  <section class="card card-front">
    <div class="front-pattern" role="img" aria-label="Faint tonal floral pattern across the soft black background"></div>
    <div class="front-lockup">
      <div class="brand-dot"></div>
      <h1 class="brand-name">Hollowmere<br>Bloom Farm</h1>
      <p class="tagline">Fresh Local Seasonal</p>
      <p class="established">EST. 2019</p>
    </div>
  </section>

  <section class="card card-back">
    <div class="back-brand">Hollowmere<br>Bloom Farm</div>
    <div class="contact-block">
      <h2 class="person-name">Tamsin Ellery Voss</h2>
      <p class="person-role">Grower</p>
      <ul class="contact-list">
        <li>website: hollowmerebloomfarm.example</li>
        <li>instagram: @hollowmerebloomfarm</li>
        <li class="gap">facebook: fb.example/hollowmereblooms/</li>
        <li>Tel: (555) 317-4290</li>
      </ul>
    </div>
  </section>
</main>
</body>
</html>
```